Brighten the Harvest marketing promotion flier!

Currently in the process of revitalizing our marketing fliers for the year 2024. Our leadership team has expressed their keen interest in embracing a rejuvenated appearance for the upcoming year. In order to achieve this, we are seeking an alternative flyer layout that effectively incorporates the same information. To provide an example, the CEO has created a mock-up of the program, along with last year's flier, solely for illustrative purposes. It is important to emphasize that we are aiming for a completely new and refreshed look.

Target Market(s)

Customers

Industry/Entity Type

roofing

Colors
0054AA
0677BA
7BADD7
CADEEF
E8F1F8
0094D4
00A9DD
6FCCEA
C7EBF8
E9F6FB

Requirements
Must have
• The information from 2023 flier
Should not have
• the same look as least year

```html
<!DOCTYPE html>
<html lang="en">
<head>
<meta charset="utf-8">
<title>Brighten the Harvest – 2024 Family &amp; Heroes Flier</title>
<link rel="stylesheet" href="https://fonts.googleapis.com/css2?family=Montserrat:ital,wght@0,600;0,700;0,800;1,800;1,900&display=swap">
<style>
  :root {
    --stage: #e4e5e7;
    --navy: #1f3a86;
    --navy-deep: #182e6c;
    --navy-light: #2a4ea3;
    --accent: #f05a28;
    --white: #ffffff;
    --box-blue: #3a66c6;
    --flag-red: #c8242f;
    --flag-blue: #1b2f78;
    --photo-riot-a: #2a3440;
    --photo-riot-b: #7d8a98;
    --photo-fire-a: #e2571c;
    --photo-fire-b: #f7b23b;
    --camo-a: #5b5a48;
    --camo-b: #8b8468;
  }
  * { margin: 0; padding: 0; box-sizing: border-box; }
  html, body {
    width: 1200px;
    height: 2692px;
    overflow: hidden;
    background: var(--stage);
    font-family: "Montserrat", Arial, sans-serif;
  }
  .flier {
    position: absolute;
    left: 0;
    top: 631px;
    width: 1200px;
    height: 1430px;
    overflow: hidden;
    background: radial-gradient(ellipse at 35% 40%, var(--navy-light) 0%, var(--navy) 45%, var(--navy-deep) 100%);
  }
  .flag {
    position: absolute;
    right: 0;
    top: 0;
    width: 420px;
    height: 980px;
    background: linear-gradient(200deg, var(--flag-red) 0%, #e8e8ee 30%, var(--flag-blue) 55%, #f4f4f8 75%, var(--flag-blue) 100%);
    clip-path: polygon(20% 0, 100% 0, 100% 100%, 62% 78%, 48% 45%, 30% 18%);
    opacity: 0.95;
  }
  .brand {
    position: absolute;
    left: 24px;
    top: 48px;
    width: 240px;
    height: 130px;
    border-radius: 50%;
    background: var(--white);
    display: flex;
    align-items: center;
    justify-content: center;
    text-align: center;
    padding: 0 26px;
  }
  .brand-name {
    font-weight: 800;
    font-size: 25px;
    line-height: 1.1;
    color: var(--navy);
  }
  .headline {
    position: absolute;
    left: 100px;
    top: 228px;
    font-weight: 800;
    font-size: 68px;
    line-height: 1.05;
  }
  .headline-year { color: var(--accent); display: block; }
  .headline-heroes {
    color: var(--white);
    display: flex;
    align-items: center;
    gap: 20px;
  }
  .headline-rule {
    display: flex;
    flex-direction: column;
    gap: 8px;
  }
  .headline-rule span {
    display: block;
    width: 120px;
    height: 4px;
    background: var(--white);
  }
  .audience {
    position: absolute;
    left: 100px;
    top: 408px;
    width: 520px;
    color: var(--white);
    font-weight: 700;
    font-size: 26px;
    line-height: 1.3;
    text-transform: uppercase;
  }
  .offer {
    position: absolute;
    left: 100px;
    top: 520px;
    color: var(--white);
    font-weight: 900;
    font-style: italic;
    font-size: 74px;
    line-height: 1;
    white-space: nowrap;
  }
  .offer-amount { color: var(--accent); }
  .offer-note {
    position: absolute;
    left: 100px;
    top: 622px;
    padding: 14px 30px;
    background: var(--box-blue);
    color: var(--white);
    font-weight: 800;
    font-size: 38px;
    letter-spacing: 0.5px;
    white-space: nowrap;
  }
  .photo {
    position: absolute;
    border: 8px solid var(--white);
    box-shadow: 0 10px 30px rgba(0,0,0,0.4);
  }
  .photo-camo {
    left: 0;
    top: 990px;
    width: 330px;
    height: 440px;
    border: none;
    box-shadow: none;
    background: linear-gradient(150deg, var(--camo-b), var(--camo-a));
    border-top-right-radius: 60% 40%;
  }
  .photo-police {
    left: 240px;
    top: 900px;
    width: 460px;
    height: 470px;
    background: linear-gradient(160deg, var(--photo-riot-b), var(--photo-riot-a));
  }
  .photo-fire {
    left: 720px;
    top: 855px;
    width: 450px;
    height: 470px;
    background: radial-gradient(circle at 35% 40%, var(--photo-fire-b), var(--photo-fire-a) 60%, #7a1f0c);
  }
</style>
</head>
<body>
  <main class="flier">
    <div class="flag" role="img" aria-label="Waving American flag with stars and stripes"></div>

    <div class="brand">
      <span class="brand-name">Brighten the Harvest</span>
    </div>

    <h1 class="headline">
      <span class="headline-year">2024 Family</span>
      <span class="headline-heroes">&amp; Heroes
        <span class="headline-rule"><span></span><span></span></span>
      </span>
    </h1>

    <p class="audience">Military, Veterans, Law Enforcement &amp; Fire Fighters</p>

    <p class="offer">Receive <span class="offer-amount">$300</span> Off</p>

    <p class="offer-note">PURCHASED MATERIALS</p>

    <div class="photo photo-camo" role="img" aria-label="Camouflage military cap"></div>
    <div class="photo photo-police" role="img" aria-label="Police officers in riot gear with helmets and shields"></div>
    <div class="photo photo-fire" role="img" aria-label="Firefighter in protective gear working in front of flames"></div>
  </main>
</body>
</html>
```